Letterhead for Business Law Firm

We need a letter head for our firm based on the design we have settled on and it is attached. Our clients are small and large businesses around the world, and our letterhead is used typically for formal legal purposes such as demand letters (accusing the recipient of doing bad things) or responding to demand letters. It may also be sent to regulators and other government agencies. So this needs to be tasteful, but a little edgy as well - we try to convey that we are a firm that is different - businesses and investors come to us for creative, quick advice, typically in high stress circumstances, and for our ability to work through high conflict situations, and rapid paced engagements.

Target Market(s)

Lawyers, business executives, investors, government regulators who may receive letters from this firm on behalf of its clients.

Industry/Entity Type

Business

Requirements
Must have
• The design and the firm's contact information:
• Quillfen Law Firm, P.C.
• 8716 SW 19th Ave
• Portland, OR 97058
• phone: 971 555 0143
• fax: 971 555 0178
• in what placement and how depicted (e.g. a phone icon instead of the word "phone") I leave to your creative ideas.
Nice to have
• design and information can be placed at the top, bottom and/or sides of the letter, and the design should be for a standard letter size paper - and can have a separate design for the second page.

```html
<!DOCTYPE html>
<html lang="en">
<head>
<meta charset="utf-8">
<title>Quillfen Law Firm, P.C. — Letterhead</title>
<link rel="stylesheet" href="https://fonts.googleapis.com/css2?family=Arimo:wght@400;700&family=Questrial&display=swap">
<style>
  :root {
    --paper: #ffffff;
    --band: #4a7178;
    --band-text: #ffffff;
    --brand-ink: #2a3638;
    --link-teal: #3f6f78;
  }
  html, body {
    margin: 0;
    padding: 0;
    overflow: hidden;
    background: var(--paper);
  }
  .letterhead {
    position: relative;
    width: 928px;
    height: 1200px;
    background: var(--paper);
    overflow: hidden;
    font-family: "Arimo", Arial, sans-serif;
  }
  .brand {
    position: absolute;
    top: 22px;
    left: 655px;
    width: 250px;
    text-align: center;
  }
  .brand-name {
    display: block;
    height: 60px;
    line-height: 60px;
    font-family: "Questrial", "Arimo", sans-serif;
    font-size: 34px;
    letter-spacing: 8px;
    color: var(--brand-ink);
    padding-left: 8px;
  }
  .brand-url {
    display: block;
    margin-top: 4px;
    font-size: 14px;
    color: var(--link-teal);
  }
  .contact-band {
    position: absolute;
    left: 0;
    bottom: 0;
    width: 928px;
    height: 72px;
    background: var(--band);
    color: var(--band-text);
    font-size: 15.5px;
  }
  .contact-item {
    position: absolute;
    top: 0;
    height: 56px;
    display: flex;
    align-items: center;
    white-space: nowrap;
  }
  .contact-item svg { flex: none; }
  .address { left: 44px; }
  .address .lines { margin-left: 9px; line-height: 19px; }
  .phone { left: 272px; }
  .phone span { margin-left: 7px; }
  .fax { left: 438px; }
  .fax b { font-weight: 700; font-size: 14px; margin-right: 4px; }
  .email { left: 609px; }
  .email span { margin-left: 12px; }
</style>
</head>
<body>
<main class="letterhead">
  <header class="brand">
    <span class="brand-name">QUILLFEN</span>
    <span class="brand-url">www.quillfen.com</span>
  </header>

  <footer class="contact-band">
    <div class="contact-item address">
      <svg width="16" height="22" viewBox="0 0 16 22" aria-hidden="true">
        <path d="M8 0C3.6 0 0 3.5 0 7.8 0 13.5 8 22 8 22s8-8.5 8-14.2C16 3.5 12.4 0 8 0z" fill="#fff"/>
        <circle cx="8" cy="7.8" r="3" fill="var(--band)"/>
      </svg>
      <div class="lines">8716 SW 19th Ave,<br>Portland, OR&nbsp; 97058</div>
    </div>

    <div class="contact-item phone">
      <svg width="28" height="28" viewBox="0 0 28 28" aria-hidden="true">
        <circle cx="14" cy="14" r="12.5" fill="none" stroke="#fff" stroke-width="1.6"/>
        <path d="M9.6 7.5c.6-.4 1.3-.3 1.7.3l1.6 2.4c.4.6.2 1.3-.3 1.7l-.9.6c.6 1.7 1.8 3.3 3.3 4.4l.8-.7c.5-.4 1.3-.4 1.7.1l2 2c.5.5.5 1.2 0 1.7l-1 1c-.8.8-2.2 1-3.3.4-3.4-1.8-6-4.7-7.3-8.3-.4-1.1-.1-2.300.7-3.1z" fill="#fff"/>
      </svg>
      <span>971 555 0143</span>
    </div>

    <div class="contact-item fax"><b>Fax :</b> 971 555 0178</div>

    <div class="contact-item email">
      <svg width="31" height="22" viewBox="0 0 31 22" aria-hidden="true">
        <path d="M1 9 15.5 0 30 9v12H1z" fill="#fff"/>
        <path d="M4 10.5 15.5 17 27 10.5" fill="none" stroke="var(--band)" stroke-width="2"/>
        <path d="M3 20 12 14M28 20 19 14" stroke="var(--band)" stroke-width="1.6"/>
      </svg>
      <span>mail@quillfen.in</span>
    </div>
  </footer>
</main>
</body>
</html>
```